New EZ Bag Modern design for Coral Tide Prawns

The frozen food category is growing, but the seafood frozen food aisle still needs an image overhaul. We have a high-quality product and we want an amazing package design to stand out as Modern, Honest, Happy, Healthy Coral Tide Prawns. Coral Tide Prawns offers a consistent superior quality shrimp. Sustainably farmed, no antibiotics ever, and responsibly sourced from Latin America (Ecuador), only from the world’s most advanced farms with the highest International Certifications. Coral Tide Prawns is peeled and packed in the U.S.A. After decades of experience in the global seafood industry and years of research and development, we built our state-of-the-art facility to bring automation and precision to every step of farmed shrimp processing.

Target Market(s)

We are targeting people that look for a great product in terms of flavor and texture. Customers that look for a product that is convenient, consistent, and healthy. Customers that look for brands that are transparent with their product and processes. Customers that want high-quality seafood at the reach of their hands, anytime.

Font styles to use
Sans Serif

Requirements
Must have
• Please read Brief.
Given the constraint we might have because of the freezers, it is essential to consider a high-impact clean design, with excellent legibility font size and coloring. The bag should communicate all our benefits from behind the glass. We want to show the real product, and there should be a window to clearly see what is inside the bag (I.Q.F. shrimp).
We want to use high-impact colors to stand compared to other products from the category (lots of white, blue, pink) and emphasize the brand.
Nice to have
• Strong, modern, clean fonts

```html
<!DOCTYPE html>
<html lang="en">
<head>
<meta charset="utf-8">
<title>Coral Tide Prawns – Raw Shrimp Bag</title>
<link href="https://fonts.googleapis.com/css2?family=Montserrat:wght@600;700;800&family=Arimo:wght@400;700&display=swap" rel="stylesheet">
<style>
  :root {
    --sky-top: #2f86d6;
    --sky-mid: #7fbde8;
    --horizon: #bfe0f2;
    --sea-top: #3a9ed6;
    --sea-deep: #0c6cb5;
    --sea-low: #1b86cb;
    --white: #ffffff;
    --ink-dark: #1d1d22;
    --brand-orange: #f26b2a;
    --band: #23252b;
    --dish: #0b0b0d;
    --shrimp-light: #e9e4e2;
    --shrimp-mid: #c9bcb8;
    --shrimp-shadow: #8d7f80;
  }
  * { box-sizing: border-box; margin: 0; padding: 0; }
  html, body { width: 1200px; height: 2673px; overflow: hidden; background: var(--white); }
  .bag {
    position: relative;
    width: 1200px;
    height: 2673px;
    overflow: hidden;
    font-family: "Arimo", Arial, sans-serif;
    color: var(--white);
  }
  .scenery-top {
    position: absolute; left: 0; top: 0; width: 1200px; height: 975px;
    background:
      radial-gradient(ellipse 520px 160px at 260px 90px, rgba(255,255,255,.75), rgba(255,255,255,0)),
      radial-gradient(ellipse 420px 140px at 900px 160px, rgba(255,255,255,.6), rgba(255,255,255,0)),
      radial-gradient(ellipse 600px 90px at 600px 520px, rgba(255,255,255,.55), rgba(255,255,255,0)),
      linear-gradient(180deg, var(--sky-top) 0%, var(--sky-mid) 40%, var(--horizon) 55%, var(--sea-top) 62%, var(--sea-deep) 100%);
  }
  .scenery-bottom {
    position: absolute; left: 0; top: 1560px; width: 1200px; height: 1113px;
    background:
      radial-gradient(ellipse 700px 120px at 600px 420px, rgba(255,255,255,.18), rgba(255,255,255,0)),
      linear-gradient(180deg, var(--sea-deep) 0%, var(--sea-low) 35%, #3d9bd6 60%, var(--sea-low) 80%, #137abf 100%);
  }
  .band { position: absolute; left: 0; width: 1200px; height: 25px; background: var(--band); }
  .band.top { top: 975px; }
  .band.bottom { top: 1536px; }
  .product-window {
    position: absolute; left: 0; top: 1000px; width: 1200px; height: 536px;
    background:
      radial-gradient(circle at 20% 40%, var(--shrimp-light), rgba(233,228,226,0) 30%),
      radial-gradient(circle at 60% 60%, var(--shrimp-light), rgba(233,228,226,0) 35%),
      radial-gradient(circle at 85% 30%, var(--shrimp-light), rgba(233,228,226,0) 30%),
      linear-gradient(135deg, var(--shrimp-mid), var(--shrimp-shadow) 50%, var(--shrimp-mid));
  }

  .brand {
    position: absolute; left: 100px; top: 240px;
    display: flex; align-items: center; gap: 22px;
  }
  .brand-dot { width: 70px; height: 70px; border-radius: 50%; background: var(--brand-orange); }
  .brand-name {
    font-family: "Montserrat", Arial, sans-serif; font-weight: 700;
    font-size: 50px; line-height: 1.05; color: var(--ink-dark); text-transform: uppercase;
  }
  .brand-tagline {
    position: absolute; left: 100px; top: 360px;
    font-size: 26px; color: var(--ink-dark);
  }

  .origin {
    position: absolute; left: 800px; top: 305px; width: 290px;
    border-top: 2px solid var(--ink-dark); border-bottom: 2px solid var(--ink-dark);
    padding: 12px 0 14px;
    font-size: 27px; line-height: 1.3; color: var(--ink-dark);
  }

  .title-block {
    position: absolute; left: 227px; top: 570px; width: 818px;
    border-top: 2px solid rgba(255,255,255,.8);
    border-bottom: 2px solid rgba(255,255,255,.8);
    height: 128px;
    display: flex; align-items: center; justify-content: center;
  }
  .title {
    font-family: "Montserrat", Arial, sans-serif; font-weight: 800;
    font-size: 100px; letter-spacing: 6px; line-height: 1; text-transform: uppercase;
  }
  .subtitle {
    position: absolute; left: 0; top: 720px; width: 1200px; text-align: center;
    font-size: 38px; line-height: 1.3;
  }
  .claim {
    position: absolute; left: 0; top: 868px; width: 1200px; text-align: center;
    font-family: "Montserrat", Arial, sans-serif; font-weight: 800;
    font-size: 56px; letter-spacing: 3px; text-transform: uppercase;
  }

  .serving { position: absolute; left: 242px; top: 1590px; width: 716px; height: 230px; }
  .serving-food {
    position: absolute; left: 440px; top: 1560px; width: 320px; height: 210px;
    border-radius: 50% 50% 45% 45%;
    background: radial-gradient(ellipse at 50% 45%, #f6b69a, #f08a6a 45%, #9cc95a 80%, rgba(156,201,90,0) 100%);
  }

  .pack-info {
    position: absolute; top: 1862px; font-size: 30px;
  }
  .pack-info.weight { left: 73px; }
  .pack-info.storage { left: 673px; }
</style>
</head>
<body>
<div class="bag">
  <div class="scenery-top" role="img" aria-label="Bright blue sky with white clouds over a calm ocean horizon"></div>
  <div class="scenery-bottom" role="img" aria-label="Calm blue ocean water reflecting light"></div>

  <div class="brand">
    <span class="brand-dot"></span>
    <span class="brand-name">Coral Tide<br>Prawns</span>
  </div>
  <p class="brand-tagline">Shrimp You Can Trust from Pond to Plate</p>

  <p class="origin">Sourced with Care<br>from Latin America<br>Peeled in the U.S.A</p>

  <div class="title-block"><h1 class="title">Raw Shrimp</h1></div>
  <p class="subtitle">Peeled &amp; Deveined / Tail Off<br>Flash Frozen to Lock in Flavor</p>
  <p class="claim">All Natural</p>

  <div class="band top"></div>
  <div class="product-window" role="img" aria-label="Clear window showing raw peeled frozen shrimp inside the bag"></div>
  <div class="band bottom"></div>

  <svg class="serving" viewBox="0 0 716 230" aria-hidden="true">
    <ellipse cx="358" cy="125" rx="356" ry="100" fill="var(--dish)"/>
  </svg>
  <div class="serving-food" role="img" aria-label="Cooked shrimp served on lettuce leaves"></div>

  <p class="pack-info weight">Net Weight 16oz (1 lb) 454g</p>
  <p class="pack-info storage">Keep Frozen-Do Not Refrigerate</p>
</div>
</body>
</html>
```